Simple and clean webdesign for personal homepage

Trying to create a simple and clean webdesign for my personal homepage. Going to use a static site builder with templates to build the site. I want it to have multiple pages - like an about me, blog and resume. I just need something very basic I can customize. I want the main colors to be purple, black and white. I am open to other color palettes too but since purple is my favorite color I want that to be one of the main colors.

The site be mostly text driven. Might have some images in the body text but I want the site design to be light and lean.

Industry/Entity Type

Personal Homepage.

Coding

Coded - Design and coding required

Number of Pages Required

1 page

Font styles to use
Sans Serif

Colors
6B429C
8869AF
B7A5CE
E3DAEB
F3F0F8

Requirements
Must have
• Clean design. Purple used as a color. HTML template.
Nice to have
• Responsive

```html
<!DOCTYPE html>
<html lang="en">
<head>
<meta charset="utf-8">
<title>Personal Blog</title>
<link href="https://fonts.googleapis.com/css2?family=Poppins:wght@400;500;600;700;800&display=swap" rel="stylesheet">
<style>
:root{
  --purple:#8a12d6;
  --purple-deep:#6b0fb3;
  --violet:#b01ee8;
  --plum:#6B429C;
  --lilac:#B7A5CE;
  --mist:#E3DAEB;
  --haze:#F3F0F8;
  --ink:#141414;
  --text:#555;
  --white:#fff;
  --grad:linear-gradient(135deg,#c21ef0 0%,#7a10d2 100%);
}
*{margin:0;padding:0;box-sizing:border-box}
html,body{width:1200px;height:5192px;overflow:hidden}
body{font-family:"Poppins",Arial,sans-serif;color:var(--ink);background:var(--white);position:relative}
.abs{position:absolute}
.ph{position:absolute;border-radius:10px}
.section-title{position:absolute;left:0;width:1200px;text-align:center;font-size:36px;font-weight:600}
.small{font-size:12px;line-height:20px;color:var(--text)}
.btn{display:inline-block;background:var(--purple);color:var(--white);border-radius:30px;font-size:13px;font-weight:600;padding:12px 26px}

/* header + hero */
.logo{left:60px;top:36px;font-size:30px;font-weight:700}
.nav{left:676px;top:40px;display:flex;gap:26px;font-size:11px;font-weight:500;color:var(--white);z-index:3}
.nav .active{border-bottom:2px solid var(--white)}
.nav-cta{left:998px;top:26px;z-index:3;padding:10px 22px;font-size:13px;background:var(--purple-deep)}
.hero-blob{left:640px;top:-260px;width:660px;height:580px;border-radius:50%;background:var(--grad)}
.hero-photo{left:656px;top:116px;width:444px;height:444px;border-radius:0 0 0 140px;background:linear-gradient(160deg,#e9e6e2,#c9c3bb 60%,#a89f95);z-index:2}
.hero-side{left:1100px;top:116px;width:36px;height:444px;border-radius:0 0 20px 0;background:var(--grad);opacity:.7}
.hero-side-text{left:1104px;top:170px;width:30px;font-size:11px;color:var(--white);writing-mode:vertical-rl}
.welcome{left:60px;top:236px;color:var(--purple);font-size:17px;font-weight:500}
.hello{left:60px;top:262px;font-size:60px;font-weight:800;line-height:70px}
.client{left:60px;top:328px;font-size:60px;font-weight:800;line-height:70px;color:var(--purple)}
.profession{left:60px;top:402px;font-size:20px;font-weight:600}
.profession span{color:var(--purple);border-bottom:2px solid var(--purple)}
.hero-copy{left:60px;top:450px;width:360px}
.follow{left:60px;top:662px;display:flex;align-items:center;gap:10px;font-size:12px;color:var(--text)}
.circle{width:30px;height:30px;border:1.5px solid var(--purple);border-radius:50%}

/* feature blog */
.feature-panel{left:232px;top:1148px;width:728px;height:272px;background:var(--haze)}
.card{position:absolute;top:872px;width:268px;height:316px;background:var(--white);box-shadow:0 6px 18px rgba(0,0,0,.08);border-radius:6px;overflow:hidden}
.card .img{height:208px}
.card .tag{position:absolute;left:18px;top:178px;background:var(--purple);color:var(--white);font-size:11px;padding:3px 14px;border-radius:4px}
.card p{padding:12px 18px;font-size:13px;line-height:19px;color:#333}
.dots{left:520px;top:1222px;display:flex;gap:10px;align-items:center}
.dots i{width:8px;height:8px;border-radius:50%;background:var(--lilac);display:block}
.dots i.on{background:var(--purple)}

/* about */
.about-circle{left:860px;top:1448px;width:400px;height:480px;border-radius:50%;background:var(--grad)}
.about-card{left:152px;top:1512px;width:880px;height:468px;background:var(--mist);border-radius:20px;box-shadow:0 10px 30px rgba(0,0,0,.08)}
.about-card::before{content:"";position:absolute;left:0;top:0;width:14px;height:100%;border-radius:20px 0 0 20px;background:var(--grad)}
.about-photo{left:692px;top:1520px;width:332px;height:452px;background:linear-gradient(170deg,#d8d8d6,#9a8f84 55%,#4c4a48);border-radius:0 0 16px 0}
.about-name{left:204px;top:1558px;font-size:30px;font-weight:600}
.about-role{left:204px;top:1604px;font-size:14px}
.about-role b{color:var(--purple);font-weight:500}
.about-copy{left:204px;top:1636px;width:440px}
.info{left:204px;top:1720px;display:grid;grid-template-columns:70px 120px 70px 150px;row-gap:8px;font-size:12px}
.info .k{color:var(--text)}
.about-btn{left:204px;top:1846px}

/* resume */
.col-title{font-size:20px;font-weight:600;border-bottom:2px solid var(--purple);padding-bottom:6px}
.res-box{position:absolute;top:2124px;width:332px;height:416px;padding:26px 24px}
.edu{background:#050505;color:var(--white)}
.exp{background:var(--grad);color:var(--white)}
.skills{background:var(--white);border:1px solid var(--mist)}
.pill{display:inline-block;background:var(--purple);color:var(--white);border-radius:20px;font-size:11px;padding:3px 14px;margin-bottom:8px}
.exp .pill{background:var(--white);color:var(--purple)}
.res-item{margin-bottom:22px}
.res-item h4{font-size:16px;font-weight:500}
.res-item p{font-size:11px;color:#ccc}
.exp .res-item p{color:#eedcff}
.skill{margin:16px 0 34px;font-size:12px;position:relative}
.bar{height:8px;background:#111;margin-top:6px;border-radius:4px;position:relative}
.bar b{position:absolute;left:0;top:0;height:8px;background:var(--purple);border-radius:4px}
.pct{position:absolute;top:-6px;background:#111;color:var(--white);font-size:10px;padding:1px 8px}

/* projects */
.proj-bg{left:0;top:2600px;width:940px;height:860px;background:var(--haze)}
.proj{position:absolute;width:284px;border-radius:14px}
.proj-over{position:absolute;inset:0;border-radius:14px;background:rgba(20,0,30,.55)}
.proj-name{position:absolute;left:20px;bottom:22px;color:var(--violet);font-size:16px;font-weight:600}
.proj-sub{position:absolute;left:20px;bottom:8px;color:#ddd;font-size:10px}

/* blog posts */
.post{position:absolute;left:168px;width:880px;height:220px}
.post .img{position:absolute;left:0;top:0;width:272px;height:220px}
.post .date{position:absolute;left:222px;top:14px;background:var(--purple);color:var(--white);font-size:11px;padding:3px 12px;border-radius:3px 0 0 3px}
.post h3{position:absolute;left:320px;top:14px;width:540px;font-size:20px;font-weight:600;line-height:28px}
.post .small{position:absolute;left:320px;top:80px;width:540px}
.read{position:absolute;left:320px;top:160px;color:var(--purple);font-size:13px;display:flex;align-items:center;gap:10px}

/* newsletter */
.news-band{left:320px;top:4560px;width:880px;height:260px;background:var(--grad);border-radius:130px 0 0 130px}
.news-photo{left:24px;top:4484px;width:380px;height:380px;border-radius:50%;background:radial-gradient(circle at 50% 40%,#d6d3cf,#8e857b 70%);border:12px solid var(--purple)}
.news-title{left:488px;top:4606px;font-size:36px;font-weight:600;color:var(--white)}
.news-copy{left:488px;top:4660px;font-size:13px;color:#f1e3ff}
.news-form{left:488px;top:4704px;width:520px;height:44px;background:var(--white);border-radius:22px;display:flex;align-items:center;justify-content:space-between;padding-left:18px;font-size:12px;color:#999}
.news-form span{background:var(--purple-deep);color:var(--white);height:44px;line-height:44px;padding:0 30px;border-radius:22px;font-weight:600}

/* footer */
.foot-logo{left:72px;top:4960px;font-size:30px;font-weight:700}
.foot-social{left:126px;top:5012px;display:flex;gap:10px}
.foot-social i{display:block;width:32px;height:32px;border-radius:50%;background:var(--purple)}
.foot-col{position:absolute;top:4904px;font-size:12px}
.foot-col h5{font-size:15px;font-weight:600;margin-bottom:12px}
.foot-col li{list-style:none;color:var(--text);line-height:20px}
.contact-row{display:flex;gap:10px;align-items:flex-start;margin-bottom:10px;color:var(--text)}
.latest{display:flex;gap:10px;margin-bottom:14px}
.latest .thumb{width:44px;height:40px;border-radius:6px;flex:none}
.latest .d{color:var(--purple);font-size:10px}
.copyright{left:0;top:5166px;width:1200px;text-align:center;font-size:11px;color:var(--text);border-top:1px solid var(--mist);padding-top:6px}
</style>
</head>
<body>

<!-- header + hero -->
<div class="abs hero-blob"></div>
<div class="abs hero-side"></div>
<div class="abs hero-side-text">Lorem ipsum dolor sit amet text</div>
<div class="abs logo">PERSONAL BLOG</div>
<nav class="abs nav"><span class="active">HOME</span><span>ABOUT ME</span><span>RESUME</span><span>PROJECTS</span><span>BLOG</span></nav>
<span class="abs btn nav-cta">CONTACT US</span>
<div class="abs hero-photo" role="img" aria-label="Photo of a man sitting with a laptop on a grey sofa"></div>
<div class="abs welcome">WELCOME TO MY WORLD</div>
<div class="abs hello">HELLO I,M</div>
<div class="abs client">CLIENT NAME</div>
<div class="abs profession">A Professional <span>Blogger</span></div>
<p class="abs hero-copy small">Lorem ipsum has been the industry's standard dummy text ever since the 1500s, when an unknown printer took a galley of type and scrambled it to make a type book.</p>
<div class="abs follow">Follow Us On <span class="circle"></span><span class="circle"></span><span class="circle"></span></div>

<!-- feature blog -->
<h2 class="section-title" style="top:774px">Feature Blog</h2>
<div class="abs feature-panel"></div>
<div class="card" style="left:-120px"><div class="img" role="img" aria-label="Blog photo of a workspace" style="background:linear-gradient(135deg,#b48a66,#5e3f28)"></div><p>Lorem ipsum has been the industry's standard dummy text ever since the</p></div>
<div class="card" style="left:172px"><div class="img" role="img" aria-label="Blog photo of a smiling woman on a phone" style="background:linear-gradient(135deg,#e8e3dc,#b7a58f)"></div><span class="tag">Health Life</span><p>Lorem ipsum has been the industry's standard dummy text ever since the when</p></div>
<div class="card" style="left:466px"><div class="img" role="img" aria-label="Blog photo of friends laughing together" style="background:linear-gradient(135deg,#d9cdbf,#8f7a65)"></div><span class="tag">Travel</span><p>Lorem ipsum has been the industry's standard dummy text ever since the</p></div>
<div class="card" style="left:760px"><div class="img" role="img" aria-label="Blog photo of a man relaxing with hands behind his head" style="background:linear-gradient(135deg,#eef0f2,#a5acb3)"></div><span class="tag">Professional</span><p>Lorem ipsum has been the industry's standard dummy text ever since the</p></div>
<div class="card" style="left:1052px"><div class="img" role="img" aria-label="Blog photo of a desk scene" style="background:linear-gradient(135deg,#cfd2d4,#6f7478)"></div><p>Lorem ipsum has been the industry's standard dummy text</p></div>
<div class="abs dots"><i></i><i></i><i class="on"></i><i></i><i></i></div>

<!-- about -->
<h2 class="section-title" style="top:1500px;left:180px;width:auto;text-align:left">About Me</h2>
<p class="abs small" style="left:180px;top:1548px">Lorem ipsum has been the industry's standard dummy text ever since the</p>
<div class="abs about-circle"></div>
<div class="abs about-card"></div>
<div class="abs about-photo" role="img" aria-label="Portrait of a bearded man in a green sweater with arms crossed"></div>
<div class="abs about-name">Client Name</div>
<div class="abs about-role">A Lead <b>Professional</b> Based in Area Name</div>
<p class="abs about-copy small">Lorem ipsum has been the industry's standard dummy text ever since the 1500s, when an unknown printer took a galley of type and scrambled it to make a specimen book that has survived.</p>
<div class="abs info">
  <span class="k">Name</span><span>Blogger Name</span><span class="k">Address</span><span>00 - lorem text print</span>
  <span class="k">Age</span><span>21 Year</span><span class="k">Phone</span><span>+0 000 0000</span>
  <span class="k">Nationality</span><span>USA</span><span class="k">Email</span><span>yourmail@example.com</span>
  <span class="k">Freelance</span><span>Available</span><span class="k">Language</span><span>French, English</span>
</div>
<span class="abs btn about-btn">DOWNLOAD CV</span>

<!-- resume -->
<div class="abs" style="left:80px;top:2056px;width:332px"><h3 class="col-title">Education</h3></div>
<div class="abs" style="left:432px;top:2056px;width:336px"><h3 class="col-title">Experience</h3></div>
<div class="abs" style="left:784px;top:2056px;width:336px"><h3 class="col-title">My Skills</h3></div>
<div class="res-box edu" style="left:80px">
  <div class="res-item"><span class="pill">2010 - 2012</span><h4>Computer Science -</h4><p>Lorem ipsum has been the industry's standard.</p></div>
  <div class="res-item"><span class="pill">2012 - 2014</span><h4>Computer Science -</h4><p>Lorem ipsum has been the industry's standard.</p></div>
  <div class="res-item"><span class="pill">2014 - 2016</span><h4>Computer Science -</h4><p>Lorem ipsum has been the industry's standard.</p></div>
</div>
<div class="res-box exp" style="left:432px;width:336px">
  <div class="res-item"><span class="pill">2016 - 2018</span><h4>Software Company</h4><p>Lorem ipsum has been the industry's standard.</p></div>
  <div class="res-item"><span class="pill">2018 - 2020</span><h4>Digital marketing</h4><p>Lorem ipsum has been the industry's standard.</p></div>
  <div class="res-item"><span class="pill">2020</span><h4>SEO</h4><p>Lorem ipsum has been the industry's standard.</p></div>
</div>
<div class="res-box skills" style="left:784px;width:336px">
  <div class="skill">Skill Name<div class="bar"><b style="width:80%"></b><span class="pct" style="left:74%">80%</span></div></div>
  <div class="skill">Skill Name<div class="bar"><b style="width:60%"></b><span class="pct" style="left:54%">60%</span></div></div>
  <div class="skill">Skill Name<div class="bar"><b style="width:70%"></b><span class="pct" style="left:64%">70%</span></div></div>
  <div class="skill">Skill Name<div class="bar"><b style="width:75%"></b><span class="pct" style="left:69%">75%</span></div></div>
  <div class="skill">Skill Name<div class="bar"><b style="width:65%"></b><span class="pct" style="left:59%">65%</span></div></div>
</div>

<!-- projects -->
<div class="abs proj-bg"></div>
<h2 class="section-title" style="top:2676px">Our Projects</h2>
<p class="abs small" style="left:0;top:2730px;width:1200px;text-align:center">Lorem ipsum has been the industry's standard dummy text ever since the</p>
<div class="proj" style="left:152px;top:2788px;height:232px;background:linear-gradient(135deg,#a13a3a,#3a1414)" role="img" aria-label="Project image of red stationery mockups"><div class="proj-over"></div><span class="proj-name">Project Name</span><span class="proj-sub">Lorem ipsum dolor</span></div>
<div class="proj" style="left:456px;top:2788px;height:232px;background:linear-gradient(135deg,#d69a6a,#3f7a6a)" role="img" aria-label="Project image of branding items on a green and tan backdrop"></div>
<div class="proj" style="left:764px;top:2788px;height:232px;background:linear-gradient(135deg,#4a4a4a,#111)" role="img" aria-label="Project image of a dark desk with devices"></div>
<div class="proj" style="left:152px;top:3092px;height:288px;background:linear-gradient(90deg,#d0d0d0 45%,#1a1a1a 55%)" role="img" aria-label="Project image of business cards on black and white"></div>
<div class="proj" style="left:456px;top:3092px;height:288px;background:linear-gradient(135deg,#f2d23a,#e94a8c 55%,#3aa6c8)" role="img" aria-label="Project image of colourful geometric print design"></div>
<div class="proj" style="left:764px;top:3092px;height:288px;background:linear-gradient(135deg,#b9e0cf,#6fb59a)" role="img" aria-label="Project image of website screens on a mint background"></div>

<!-- blog posts -->
<h2 class="section-title" style="top:3516px">BLOG POST</h2>
<div class="post" style="top:3636px"><div class="img ph" style="border-radius:0;background:linear-gradient(135deg,#a8b4bc,#5e5146)" role="img" aria-label="Photo of a man with a backpack on a city street"></div><span class="date">11 Jan</span><h3>Lorem Ipsum Is Simply Dummy Text Of The Printing And Typesetting Industry</h3><p class="small">Lorem ipsum has been the industry's standard dummy text ever since the 1500s, when an unknown printer took a galley of type and scrambled it to make a type specimen book. It has survived not only five centuries.</p><span class="read">Read More <svg width="30" height="10"><path d="M0 5h28M23 1l5 4-5 4" stroke="#8a12d6" fill="none" stroke-width="1.5"/></svg></span></div>
<div class="post" style="top:3900px"><div class="img ph" style="border-radius:0;background:linear-gradient(135deg,#3a3340,#b08a8a)" role="img" aria-label="Photo of a woman in front of a ring light"></div><span class="date">11 Jan</span><h3>Lorem Ipsum Is Simply Dummy Text Of The Printing And Typesetting Industry</h3><p class="small">Lorem ipsum has been the industry's standard dummy text ever since the 1500s, when an unknown printer took a galley of type and scrambled it to make a type specimen book. It has survived not only five centuries.</p><span class="read">Read More <svg width="30" height="10"><path d="M0 5h28M23 1l5 4-5 4" stroke="#8a12d6" fill="none" stroke-width="1.5"/></svg></span></div>
<div class="post" style="top:4160px"><div class="img ph" style="border-radius:0;background:linear-gradient(135deg,#d9a04a,#6a4a3a)" role="img" aria-label="Photo of a man filming with a camera"></div><span class="date">11 Jan</span><h3>Lorem Ipsum Is Simply Dummy Text Of The Printing And Typesetting Industry</h3><p class="small">Lorem ipsum has been the industry's standard dummy text ever since the 1500s, when an unknown printer took a galley of type and scrambled it to make a type specimen book. It has survived not only five centuries.</p><span class="read">Read More <svg width="30" height="10"><path d="M0 5h28M23 1l5 4-5 4" stroke="#8a12d6" fill="none" stroke-width="1.5"/></svg></span></div>
<div class="abs" style="left:0;top:4470px;width:1200px;text-align:center;font-size:13px;color:var(--purple)"><span style="border-bottom:1px solid var(--purple)">Explore more</span></div>

<!-- newsletter -->
<div class="abs news-band"></div>
<div class="abs news-photo" role="img" aria-label="Portrait of a smiling bearded man with glasses"></div>
<div class="abs news-title">Saty Upto Date With Us !</div>
<div class="abs news-copy">Would you like to receive our exclusive update for subscribe today !</div>
<div class="abs news-form">Enter Email *<span>SUBSCRIBE</span></div>

<!-- footer -->
<div class="abs foot-logo">PERSONAL BLOG</div>
<div class="abs foot-social"><i></i><i></i><i></i></div>
<div class="foot-col" style="left:336px"><h5>SITEMAP</h5><ul><li>Home</li><li>About Us</li><li>Resume</li><li>Projects</li><li>Blog</li><li>Contact Us</li></ul></div>
<div class="foot-col" style="left:612px;width:230px"><h5>CONTACT US</h5>
  <div class="contact-row"><svg width="14" height="14" viewBox="0 0 24 24"><path d="M6.6 10.8a15 15 0 0 0 6.6 6.6l2.2-2.2a1 1 0 0 1 1-.25 11 11 0 0 0 3.6.6 1 1 0 0 1 1 1V20a1 1 0 0 1-1 1A17 17 0 0 1 3 4a1 1 0 0 1 1-1h3.5a1 1 0 0 1 1 1 11 11 0 0 0 .6 3.6 1 1 0 0 1-.25 1z" fill="#8a12d6"/></svg>123 456 7890</div>
  <div class="contact-row"><svg width="14" height="14" viewBox="0 0 24 24"><rect x="2" y="5" width="20" height="14" rx="2" fill="#8a12d6"/><path d="M2 7l10 6 10-6" stroke="#fff" fill="none" stroke-width="1.5"/></svg>yourmail@example.com</div>
  <div class="contact-row"><svg width="14" height="14" viewBox="0 0 24 24"><path d="M12 2a7 7 0 0 0-7 7c0 5 7 13 7 13s7-8 7-13a7 7 0 0 0-7-7zm0 9.5A2.5 2.5 0 1 1 12 6.5a2.5 2.5 0 0 1 0 5z" fill="#8a12d6"/></svg><span>Personal Blogger<br>Lorem ipsum simple text print type setting industry</span></div>
</div>
<div class="foot-col" style="left:888px;width:240px"><h5>LATEST BLOG</h5>
  <div class="latest"><div class="thumb" style="background:linear-gradient(135deg,#c9b9a6,#6d5a48)" role="img" aria-label="Thumbnail of a blog photo"></div><div><div class="d">11 January 2022</div><div class="small" style="line-height:15px">Lorem ipsum simple text print type setting</div></div></div>
  <div class="latest"><div class="thumb" style="background:linear-gradient(135deg,#d6c4b0,#7a5e4a)" role="img" aria-label="Thumbnail of a blog photo"></div><div><div class="d">11 January 2022</div><div class="small" style="line-height:15px">Lorem ipsum simple text print type setting</div></div></div>
</div>
<div class="abs copyright">PERSONAL BLOG - 2022 All rights reserved</div>

</body>
</html>
```